Reaching the Root: Reasoning in Clinical Choice-Making

I'd like a cover that looks like it would fit on the shelf next to "The Symptom Mirage" by Harold Vintner, "The Fall of Forgetting" by Carl Mortenson, "Meal Mend" by Neil Forsby, "The Energy Renewal Plan" by Owen Prichardson or "The Gland Renewal Plan" by the same or "The Cortex Renewal Plan" by the same ... either text only (with some interesting fonts that make the title stand out, and the subtitle smaller) or a relevant image, though I'm not entirely sure what that would be since this is a book about big-picture medical decision making.
Author name is Dr Miriam Oakhurst, NMD
I'll eventually request an e-book, paperback, and audio cover from the winner...

Target Market(s)

practicing physicians

Industry/Entity Type

medicine

Requirements
Must have
• look similar to other books in the genre

```html
<!DOCTYPE html>
<html lang="en">
<head>
<meta charset="utf-8">
<title>Reaching the Root: Reasoning in Clinical Choice-Making</title>
<link href="https://fonts.googleapis.com/css2?family=Cinzel:wght@400;500&family=Arimo:wght@400&display=swap" rel="stylesheet">
<style>
  :root {
    --paper: #f9f9fa;
    --navy: #00284f;
    --navy-soft: #1f3f63;
    --crimson: #7b1c22;
    --mist: #e4e9ef;
  }
  html, body {
    margin: 0;
    padding: 0;
    overflow: hidden;
    background: var(--paper);
  }
  .cover {
    position: relative;
    width: 800px;
    height: 1200px;
    background: var(--paper);
    overflow: hidden;
  }
  .rule {
    position: absolute;
    left: 78px;
    width: 645px;
    height: 2px;
    background: var(--crimson);
  }
  .rule--top { top: 138px; left: 80px; width: 643px; }
  .rule--author-above { top: 1048px; }
  .rule--author-below { top: 1133px; }

  .series {
    position: absolute;
    top: 74px;
    left: 0;
    width: 800px;
    margin: 0;
    text-align: center;
    font-family: "Cinzel", serif;
    font-weight: 400;
    font-size: 52px;
    line-height: 1;
    letter-spacing: 3px;
    color: var(--crimson);
    white-space: nowrap;
  }
  .title {
    margin: 0;
    font-family: "Cinzel", serif;
    font-weight: 500;
    color: var(--navy);
  }
  .title__line {
    position: absolute;
    left: 0;
    width: 800px;
    text-align: center;
    line-height: 1;
    white-space: nowrap;
    display: block;
  }
  .title__line--first { top: 196px; font-size: 78px; letter-spacing: 1px; }
  .title__line--main { top: 290px; font-size: 120px; }
  .title__line--last { top: 428px; font-size: 68px; letter-spacing: 1px; }

  .emblem {
    position: absolute;
    left: 175px;
    top: 548px;
    width: 460px;
    height: 460px;
    border-radius: 50%;
    background: radial-gradient(circle at 50% 50%, var(--navy-soft) 0%, #6c85a3 35%, var(--mist) 70%, var(--paper) 100%);
  }

  .author {
    position: absolute;
    top: 1066px;
    left: 0;
    width: 800px;
    margin: 0;
    text-align: center;
    font-family: "Arimo", Arial, sans-serif;
    font-weight: 400;
    font-size: 46px;
    line-height: 1;
    color: var(--navy);
    white-space: nowrap;
  }
</style>
</head>
<body>
  <main class="cover">
    <p class="series">REACHING THE ROOT</p>
    <div class="rule rule--top"></div>

    <h1 class="title">
      <span class="title__line title__line--first">REASONING IN</span>
      <span class="title__line title__line--main">CLINICAL</span>
      <span class="title__line title__line--last">CHOICE-MAKING</span>
    </h1>

    <div class="emblem" role="img" aria-label="Compass rose with a red and teal needle pointing north, in navy line work"></div>

    <div class="rule rule--author-above"></div>
    <p class="author">Dr. Miriam Oakhurst, NMD</p>
    <div class="rule rule--author-below"></div>
  </main>
</body>
</html>
```